Tax Firm - Creative Print Ads to Build New Clients

I'm the marketing director of an integrated financial services business based in Melbourne Australia. I need to create a series of 4 press ads to run in the local business newspaper.

Each ad needs to stand alone, but at the same time should appear visually as from the same company and be part of a series.

The ad will will 115mm by 255mm (1/3 of a page horizontal)

Final artwork needs to be setup using CMYK and at the exact dimensions no bleed.

Brief
- Our tax practice provides services to individuals & small businesses (cafes, tradespeoeple, retailers)
- Our tagline is Bold, Proactive, Strategic, Practical financial advice, Chart Your Course (a brand logo will be provided)
- The company logo needs to be included
- Web address included
- phone number included
- The ad needs to be professional, yet energetic
- Stock photography should be at an absolute minimum where models are not identifable
- Graphics are prefered over stock images
- Sketches are great
- Key message - we do tax returns, we care about you as an individual, we've been in the Docklands for 20 years, we are your local partner in your financial journey
Updates

Target Market(s)

Individuals earning between 50,000 and 200,000 per annum

Industry/Entity Type

Accounting

Font styles to use
Sans Serif
Script

Colors
3176b5
1b1b1b
fbf289
ec1f27
85acd3
0355a3

Requirements
Must have
• Sell t services to individuals as primary audience, with small businesses as a secondary audience.
• ---- Updated ----
• The company is www.brellacove.com.au
• I've added
• - logos (vertical, horizontal, reverse and our brand tagline too)
• - Brand Guidelines
Nice to have
• I want to see some graphics that sell the idea that we are a local firm with 20 years experience in the area.
• We care about individuals first
Should not have
• Avoid using stock images where the pretty model is identifiable, we hate to see actors in our ads

```html
<!DOCTYPE html>
<html lang="en">
<head>
<meta charset="utf-8">
<title>Brellacove – Tax Press Ad</title>
<link rel="stylesheet" href="https://fonts.googleapis.com/css2?family=Mukta:wght@400;500;600&family=Montserrat:wght@700&family=Caveat:wght@500&display=swap">
<style>
  :root {
    --brand-blue: #3176b5;
    --ink: #1b1b1b;
    --highlight: #fbf289;
    --sky: #85acd3;
    --deep-blue: #0355a3;
    --paper: #ffffff;
    --scene-tone: #5b93c8;
  }
  html, body {
    margin: 0;
    padding: 0;
    width: 946px;
    height: 1200px;
    overflow: hidden;
    background: var(--paper);
  }
  .canvas {
    position: relative;
    width: 946px;
    height: 1200px;
    font-family: "Mukta", "Helvetica Neue", Arial, sans-serif;
  }
  .ad-shapes {
    position: absolute;
    left: 0;
    top: 0;
  }
  .brand-name {
    position: absolute;
    left: 232px;
    top: 196px;
    width: 130px;
    text-align: center;
    margin: 0;
    color: var(--paper);
    font-size: 14px;
    font-weight: 400;
    letter-spacing: 3px;
  }
  .brand-values {
    position: absolute;
    left: 393px;
    top: 103px;
    margin: 0;
    color: var(--paper);
    font-family: "Montserrat", Arial, sans-serif;
    font-weight: 700;
    font-size: 10.5px;
    letter-spacing: 1.3px;
    word-spacing: 3px;
  }
  .brand-motto {
    position: absolute;
    left: 610px;
    top: 116px;
    margin: 0;
    color: var(--paper);
    font-family: "Caveat", cursive;
    font-size: 13px;
    transform: rotate(-6deg);
    transform-origin: left center;
  }
  .headline {
    position: absolute;
    left: 301px;
    top: 262px;
    margin: 0;
    color: var(--paper);
    font-size: 27px;
    font-weight: 500;
    line-height: 34px;
  }
  .headline .accent { color: var(--highlight); }
  .team-title {
    position: absolute;
    left: 247px;
    top: 736px;
    margin: 0;
    font-size: 22px;
    line-height: 26px;
    font-weight: 500;
    color: var(--ink);
  }
  .team-title .sub { display: block; color: var(--brand-blue); }
  .team-rule {
    position: absolute;
    left: 247px;
    top: 799px;
    width: 387px;
    height: 3px;
    background: var(--highlight);
  }
  .team-copy {
    position: absolute;
    left: 247px;
    top: 810px;
    width: 380px;
    margin: 0;
    font-size: 16px;
    line-height: 24.5px;
    color: var(--ink);
  }
  .team-copy .year { color: var(--brand-blue); }
  .call-prompt {
    position: absolute;
    right: 278px;
    top: 925px;
    margin: 0;
    text-align: right;
    color: var(--paper);
    font-size: 17px;
    font-weight: 500;
    line-height: 23px;
  }
  .phone {
    position: absolute;
    right: 278px;
    top: 982px;
    margin: 0;
    color: var(--highlight);
    font-size: 29px;
    font-weight: 500;
    letter-spacing: 0.5px;
  }
  .web {
    position: absolute;
    left: 361px;
    top: 1038px;
    width: 336px;
    height: 47px;
    line-height: 50px;
    margin: 0;
    text-align: center;
    background: var(--highlight);
    border-radius: 12px 0 0 12px;
    color: var(--brand-blue);
    font-size: 22px;
    font-weight: 500;
  }
</style>
</head>
<body>
<div class="canvas">
  <svg class="ad-shapes" width="946" height="1200" viewBox="0 0 946 1200" aria-hidden="false">
    <rect class="ad-frame" x="220" y="60" width="477" height="1057" fill="var(--paper)" stroke="#d9d9d9" stroke-width="1"/>
    <rect class="top-rule" x="220" y="60" width="477" height="2.5" fill="var(--brand-blue)"/>

    <rect class="hero-panel" x="220" y="166" width="477" height="554" fill="var(--brand-blue)"/>
    <path class="hero-notch" d="M697,575 L596,575 Q578,575 578,593 L578,720 L697,720 Z" fill="var(--paper)"/>

    <path class="header-band" d="M220,62 L697,62 L697,166 L396,166 Q376,166 376,186 L376,205 Q376,228 350,232 Q270,242 220,266 Z" fill="var(--ink)"/>
    <path class="header-swoosh" d="M220,342 Q236,262 330,237 Q262,248 220,268 Z" fill="var(--highlight)"/>

    <circle class="brand-dot" cx="297" cy="130" r="30" fill="none" stroke="var(--paper)" stroke-width="3"/>

    <g class="hero-scene" role="img" aria-label="Flat illustration of hands around a desk with money, a phone, financial charts, an envelope, calculator, pens and a notepad">
      <rect x="548" y="180" width="149" height="140" rx="10" fill="var(--scene-tone)"/>
      <rect x="222" y="365" width="470" height="206" rx="10" fill="var(--scene-tone)"/>
      <rect x="222" y="560" width="350" height="160" rx="10" fill="var(--scene-tone)"/>
    </g>

    <path class="contact-panel" d="M657,720 Q635,720 635,742 L635,876 Q635,900 611,900 L359,900 Q335,900 335,924 L335,1011 Q335,1035 311,1035 L220,1035 L220,1117 L697,1117 L697,720 Z" fill="var(--brand-blue)"/>
  </svg>

  <p class="brand-name">BRELLACOVE</p>
  <p class="brand-values">BOLD PROACTIVE STRATEGIC PRACTICAL</p>
  <p class="brand-motto">Chart Your Course</p>

  <h1 class="headline">Pay the tax<br>you’re obliged to<br><span class="accent">but nothing more!</span></h1>

  <h2 class="team-title">WE ARE TEAM<span class="sub">we care about your situation</span></h2>
  <div class="team-rule"></div>
  <p class="team-copy">Will ensure you get the expert advice to meet your needs today, but will ensure we've considered the coming <span class="year">1</span>, <span class="year">3</span>, <span class="year">5</span> and <span class="year">10</span> years</p>

  <p class="call-prompt">Just give us a call before you make<br>a tax decision</p>
  <p class="phone">03 9555 0142</p>
  <p class="web">www.brellacove.com.au</p>
</div>
</body>
</html>
```